Free offer card

I need a business card sized FREE CLASS offer thing....Our target market is 18-40 year old women. We are the "sexy" pole studio but don't want to scare people off. This card will be given out by students and staff when they meet people that are interested and also put in hair dressers and sports shops etc. I've got HEAPS of photos so I'll upload a few, I'll also upload the last brochure we did but I'm not sure it's really doing it's job....might be a little scary? The free trial class maybe wasn't clear enough. I think maybe free class instead of using the word "trial" so they don't think they are going to get a hard sell. Need a space we can write student/teachers name on it...maybe Marlo's Muse_________
And need both studios details on it (on attached brochure) happy to send different photos if it helps
I can get high res stuff and better copies of the fit fierce sexy brochure if you want...haven't used this website before not really sure what you need

```html
<!DOCTYPE html>
<html lang="en">
<head>
<meta charset="utf-8">
<title>Marlo's Pole Studio – Free Class Card</title>
<link href="https://fonts.googleapis.com/css2?family=Audiowide&family=Courgette&family=Open+Sans:wght@400&display=swap" rel="stylesheet">
<style>
  :root {
    --backdrop: #d8d8d8;
    --charcoal: #3c3c3c;
    --magenta: #c8106e;
    --magenta-deep: #a80c5c;
    --blush: #f7dbe8;
    --blush-light: #f6e6ef;
    --ink: #222222;
    --white: #ffffff;
  }
  * { box-sizing: border-box; margin: 0; padding: 0; }
  html, body { width: 1200px; height: 1200px; overflow: hidden; }
  body { background: var(--backdrop); position: relative; font-family: "Open Sans", sans-serif; }

  .card {
    position: absolute; top: 174px; width: 520px; height: 851px;
    background: linear-gradient(90deg, var(--blush) 0%, var(--blush-light) 50%, var(--blush) 100%);
    overflow: hidden;
  }
  .card--front { left: 54px; }
  .card--back { left: 630px; }

  .card__header {
    position: absolute; left: 0; top: 0; width: 100%; height: 160px;
    background: var(--charcoal);
  }
  .brand-name {
    position: absolute; left: 30px; top: 26px;
    font-family: "Audiowide", sans-serif; color: var(--white);
    font-size: 52px; line-height: 58px; letter-spacing: 1px;
  }

  .card__footer {
    position: absolute; left: 0; bottom: 0; width: 100%; height: 144px;
    background: linear-gradient(180deg, var(--magenta-deep), var(--magenta));
  }

  .photo-frame { position: absolute; left: 32px; top: 170px; width: 460px; height: 460px; }

  .offer-title {
    position: absolute; left: 0; top: 652px; width: 100%; text-align: center;
    font-family: "Audiowide", sans-serif; font-size: 38px; color: var(--magenta);
    -webkit-text-stroke: 1px #3a0d24; letter-spacing: -1px;
  }

  .holder-label {
    position: absolute; left: 0; top: 4px; width: 100%; text-align: center;
    font-family: "Courgette", cursive; font-size: 46px; color: var(--white);
  }
  .name-field {
    position: absolute; left: 34px; top: 72px; width: 451px; height: 58px;
    background: var(--white); border-radius: 29px;
  }

  .studio { position: absolute; left: 0; width: 100%; text-align: center; color: var(--ink); }
  .studio--city { top: 204px; }
  .studio--bayside { top: 444px; }
  .studio__name { font-family: "Audiowide", sans-serif; font-size: 34px; line-height: 48px; }
  .studio__rule { width: 228px; height: 3px; background: var(--magenta); margin: 10px auto 16px; }
  .studio__details { font-size: 31px; line-height: 40px; letter-spacing: 1px; }

  .contact { position: absolute; left: 0; width: 100%; text-align: center; color: var(--white); }
  .contact--email { top: 36px; font-size: 29px; letter-spacing: 0.5px; }
  .contact--web { top: 88px; font-size: 25px; }
</style>
</head>
<body>

<section class="card card--front">
  <header class="card__header">
    <div class="brand-name">Marlo's<br>Pole Studio</div>
  </header>

  <svg class="photo-frame" viewBox="0 0 460 460" role="img" aria-label="Photograph of a pole dancer in an inverted pose on a pole">
    <defs>
      <linearGradient id="ring" x1="0" y1="0" x2="0" y2="1">
        <stop offset="0" stop-color="#2a2a2a"/>
        <stop offset="0.35" stop-color="#d4157a"/>
        <stop offset="0.7" stop-color="#c8106e"/>
        <stop offset="1" stop-color="#2a2a2a"/>
      </linearGradient>
      <radialGradient id="photoFill" cx="0.5" cy="0.5" r="0.5">
        <stop offset="0" stop-color="#f6e7ef"/>
        <stop offset="0.7" stop-color="#e9c9d8"/>
        <stop offset="1" stop-color="#b98aa0"/>
      </radialGradient>
    </defs>
    <circle cx="230" cy="230" r="215" fill="url(#photoFill)"/>
    <circle cx="230" cy="230" r="221" fill="none" stroke="url(#ring)" stroke-width="16"/>
  </svg>

  <div class="offer-title">FREE CLASS VAUCHER</div>

  <footer class="card__footer">
    <div class="holder-label">Marlo's Muse</div>
    <div class="name-field"></div>
  </footer>
</section>

<section class="card card--back">
  <header class="card__header">
    <div class="brand-name">Marlo's<br>Pole Studio</div>
  </header>

  <div class="studio studio--city">
    <h2 class="studio__name">CITY STUDIO</h2>
    <div class="studio__rule"></div>
    <p class="studio__details">Level 2, 84 Carrow St,<br>Sydney NSW 2000<br>(02) 9100-4512</p>
  </div>

  <div class="studio studio--bayside">
    <h2 class="studio__name">BAYSIDE STUDIO</h2>
    <div class="studio__rule"></div>
    <p class="studio__details">5/212 Tidewater Rd,<br>Bayview NSW 2230<br>(02) 9100-7786</p>
  </div>

  <footer class="card__footer">
    <p class="contact contact--email">hello@marlospolestudio.com.au</p>
    <p class="contact contact--web">WWW.MARLOSPOLESTUDIO.COM.AU</p>
  </footer>
</section>

</body>
</html>
```